Fern Lusk medical cannibis cultivation company

tag - Lusk grow
Fern Lusk medical cannabis cultivation - logo is selected- can we please see bold examples with our selection. We are mainly dealing with medical companies and professionals. We would like to be stand out in the crowd with our designs. Welcome any and all attempts. Thanks

Target Market(s)

Medical and Professional

Industry/Entity Type

Medical And Science

Font styles to use
Sans Serif

Colors

Designer to choose colors to be used in the design.

Requirements
Must have
• Bright colour and be bold- Love the teal and magenta that is currently on the dark background design.
Nice to have
• shading and the 3D affect- The shadowed appearance.
Should not have
• Anything related to illegal activity or un professional manners

```html
<!DOCTYPE html>
<html lang="en">
<head>
<meta charset="utf-8">
<title>Fern Lusk Stationery</title>
<link href="https://fonts.googleapis.com/css2?family=Didact+Gothic&family=Arimo:wght@400&display=swap" rel="stylesheet">
<style>
  :root{
    --teal:#1db0e6;
    --magenta:#a6409b;
    --ink:#3a3a3a;
    --grey:#8a8a8a;
    --backdrop:#dedede;
    --paper:#f6f6f6;
    --flap:#050505;
  }
  *{margin:0;padding:0;box-sizing:border-box}
  html,body{width:1200px;height:877px;overflow:hidden;background:var(--backdrop)}
  .canvas{position:relative;width:1200px;height:877px}

  .sheet{position:absolute;background:var(--paper);overflow:hidden}
  .letterhead{left:61px;top:66px;width:527px;height:742px}
  .envelope-back{left:614px;top:298px;width:532px;height:242px}
  .envelope-front{left:616px;top:567px;width:530px;height:241px}

  .ribbon{position:absolute;background:var(--teal)}
  .brand-circle{position:absolute;border-radius:50%;border:3px solid #9a9a9a;background:var(--paper)}
  .brand-name{position:absolute;font-family:"Didact Gothic",sans-serif;color:var(--teal);font-size:16px;letter-spacing:.3px;white-space:nowrap}

  .watermark{position:absolute;opacity:.35;border-radius:50% 50% 46% 46%;
    background:radial-gradient(ellipse at 45% 55%, rgba(166,64,155,.28), rgba(29,176,230,.22) 55%, rgba(29,176,230,0) 75%)}

  .contact{position:absolute;left:386px;top:40px;font-family:Arimo,sans-serif;font-size:8.8px;line-height:10.6px;color:var(--ink)}
  .contact .address{margin-bottom:3px}
  .contact-row{display:flex;align-items:center;gap:5px;height:11px}
  .contact-row svg{width:8px;height:8px;fill:var(--teal);flex:none}

  .letter{position:absolute;left:46px;top:0;width:438px;font-family:"Didact Gothic",sans-serif;color:var(--ink)}
  .salutation{position:absolute;top:207px;font-size:13.5px;color:#444}
  .body{position:absolute;top:245px;width:438px;font-size:7.6px;line-height:11.4px;text-align:justify}
  .body p{margin-bottom:11.4px}
  .closing{position:absolute;top:484px;font-size:7.6px}
  .signature{position:absolute;left:46px;top:520px;width:90px;height:38px;border-radius:4px;
    background:linear-gradient(90deg,rgba(40,70,160,.18),rgba(40,70,160,.06))}

  .flap{position:absolute;left:0;top:0;width:532px;height:75px}
  .flap-name{position:absolute;left:266px;top:32px;transform:translateX(-50%);font-family:"Didact Gothic",sans-serif;font-size:10px;color:var(--teal);letter-spacing:.3px}

  .return-address{position:absolute;left:31px;top:106px;font-family:Arimo,sans-serif;font-size:8.8px;line-height:10.6px;color:var(--ink)}
</style>
</head>
<body>
<main class="canvas">

  <section class="sheet letterhead">
    <div class="watermark" role="img" aria-label="Faint large brand leaf decoration" style="left:195px;top:182px;width:295px;height:448px"></div>
    <div class="ribbon" style="left:66px;top:0;width:53px;height:58px"></div>
    <div class="brand-circle" style="left:63px;top:41px;width:58px;height:58px"></div>
    <div class="brand-name" style="left:46px;top:96px">FERN LUSK</div>

    <div class="contact">
      <div class="address">4120 Alder Ridge Road<br>Juneau, Alaska 99801</div>
      <div class="contact-row"><svg viewBox="0 0 10 10"><path d="M2 0.5l2 2-1 1.2c.6 1.3 1.8 2.5 3.1 3.1l1.2-1 2 2-1.3 1.7C4.5 9.3.7 5.5.3 1.8z"/></svg>555 210 4471</div>
      <div class="contact-row"><svg viewBox="0 0 10 10"><path d="M2.5 0h5v10h-5zM3.5 1v7h3V1z"/></svg>555 318 2096</div>
      <div class="contact-row"><svg viewBox="0 0 10 10"><path d="M2 0h6v3H2zM0 3.5h10V8H8v2H2V8H0zM3 6.5v2.5h4V6.5z"/></svg>555 742 6630</div>
      <div class="contact-row"><svg viewBox="0 0 10 10"><path d="M0 2h10v6H0zM1 3l4 3 4-3v-.3H1z"/></svg>ivan@fernlusk.com</div>
      <div class="contact-row"><svg viewBox="0 0 10 10"><circle cx="5" cy="5" r="5"/><path d="M2 3.5h6M1.5 6.5h7M5 0.5v9" stroke="#fff" stroke-width=".8" fill="none"/></svg>www.fernlusk.com</div>
    </div>

    <div class="letter">
      <div class="salutation">Dear Mr. Harlow,</div>
      <div class="body">
        <p>Lorem ipsum dolor sit amet, consectetur adipiscing elit. Donec orci purus, luctus vitae dignissim eu, iaculis sed purus. Vivamus faucibus, ipsum nec aliquet viverra, leo mauris condimentum ligula, sit amet sagittis enim ligula quis arcu. Nam egestas tortor id nisi porttitor mattis. In tortor ante, ultricies in suscipit a, tempus non massa. Vivamus et auctor mi. Fusce vel massa nulla. Phasellus nec eros mauris, et scelerisque orci.</p>
        <p>Donec malesuada orci vitae nulla accumsan porta a id massa. Quisque accumsan iaculis magna sit amet fringilla. Maecenas consequat, magna eget tincidunt semper, odio nibh rutrum mi, id feugiat ante nisi eu risus. Vestibulum nunc orci, rhoncus a placerat in, ultricies in mi. Cras mattis varius eros, vel fringilla nisi suscipit eget. Quisque scelerisque sagittis nulla at porttitor.</p>
        <p>Sed id augue vitae urna euismod commodo aliquet a quam. Pellentesque arcu velit, cursus et malesuada ut, consequat et diam. Nullam erat sem, rhoncus id ullamcorper vitae, rhoncus et arcu. In ultricies ultricies nulla, ut rutrum nisi iaculis at. Donec eu magna a metus ornare faucibus. Fusce aliquet faucibus ultricies. Morbi semper, est id tincidunt gravida, sem arcu adipiscing lacus, ac bibendum nulla leo eu purus. Quisque nec diam sed risus consectetur a ccumsan quis quis nibh. Vestibulum id purus lorem.</p>
        <p>It is a long established fact that a reader will be distracted by the readable content of a page when looking at its layout. The point of using Lorem Ipsum is that it has a more-or-less normal distribution of letters, as opposed to using 'Content here, content here', making it look like readable English. Many desktop publishing packages</p>
      </div>
      <div class="closing">Sincerely,</div>
    </div>
    <div class="signature" role="img" aria-label="Handwritten signature of Ivan Harlow"></div>
  </section>

  <section class="sheet envelope-back">
    <svg class="flap" viewBox="0 0 532 75" aria-hidden="true">
      <path d="M0 0H532L524 53Q521 75 499 75H33Q11 75 8 53Z" fill="var(--flap)"/>
    </svg>
    <div class="flap-name">FERN LUSK</div>
  </section>

  <section class="sheet envelope-front">
    <div class="watermark" role="img" aria-label="Faint brand leaf decoration" style="left:328px;top:9px;width:192px;height:224px"></div>
    <div class="ribbon" style="left:50px;top:0;width:53px;height:42px"></div>
    <div class="brand-circle" style="left:48px;top:25px;width:57px;height:57px"></div>
    <div class="brand-name" style="left:31px;top:79px">FERN LUSK</div>
    <div class="return-address">4120 Alder Ridge Road<br>Juneau, Alaska 99801</div>
  </section>

</main>
</body>
</html>
```